Die Designerin hat meine Vorstellungen am besten verstanden und umgesetzt. Sie war mir gegenüber sehr verständnisvoll und entgegenkommend. Die Kommunikation mit ihr war sehr erfreulich und sympathisch. Bei meinem nächsten Projekt werde ich mich zuerst an sie wenden.

```html
<!DOCTYPE html>
<html lang="de">
<head>
<meta charset="utf-8">
<title>Mein wunderbarer Sommer in Weilertal – Buchumschlag</title>
<link rel="stylesheet" href="https://fonts.googleapis.com/css2?family=Cinzel:wght@400;600;700&display=swap">
<style>
  :root {
    --backdrop: #d21d12;
    --cover-blue: #4552b2;
    --cover-blue-deep: #3a47a6;
    --title-light: #b9d6ee;
    --title-mid: #8fbde4;
    --title-accent: #5ab9de;
    --cream: #f6e3c4;
    --scooter-red: #e8391c;
    --scooter-orange: #f28a2a;
    --shadow-blue: #3340a0;
  }
  * { margin: 0; padding: 0; box-sizing: border-box; }
  html, body {
    width: 1200px;
    height: 1055px;
    overflow: hidden;
  }
  body {
    background: var(--backdrop);
    font-family: "Cinzel", "Times New Roman", serif;
    position: relative;
  }
  .book-cover {
    position: absolute;
    left: 282px;
    top: 23px;
    width: 677px;
    height: 1008px;
    background: radial-gradient(ellipse at 50% 35%, var(--cover-blue) 0%, var(--cover-blue-deep) 100%);
    overflow: hidden;
  }
  .genre-label,
  .title-line,
  .author-name {
    position: absolute;
    left: 0;
    width: 100%;
    text-align: center;
    line-height: 1;
    white-space: nowrap;
  }
  .genre-label {
    top: 5px;
    font-weight: 700;
    font-size: 30px;
    letter-spacing: 1px;
    color: var(--cream);
  }
  .book-title { font-weight: 400; }
  .title-small {
    color: var(--title-accent);
    font-size: 56px;
    letter-spacing: 8px;
  }
  .title-large {
    color: var(--title-light);
    font-size: 76px;
    letter-spacing: 7px;
  }
  .title-mein { top: 77px; }
  .title-main { top: 120px; color: var(--title-mid); }
  .title-season { top: 191px; }
  .title-in { top: 271px; }
  .title-place { top: 318px; }
  .cover-illustration {
    position: absolute;
    left: 81px;
    top: 407px;
    width: 520px;
    height: 440px;
    background:
      radial-gradient(ellipse 45% 40% at 48% 55%, var(--scooter-red) 0%, var(--scooter-orange) 45%, rgba(242,138,42,0) 75%),
      linear-gradient(160deg, rgba(51,64,160,0) 40%, var(--shadow-blue) 100%);
    border-radius: 40px;
  }
  .author-name {
    top: 909px;
    font-weight: 700;
    font-size: 29px;
    letter-spacing: 9px;
    color: var(--cream);
  }
</style>
</head>
<body>
  <main class="book-cover">
    <p class="genre-label">ROMAN</p>
    <h1 class="book-title">
      <span class="title-line title-small title-mein">MEIN</span>
      <span class="title-line title-large title-main">WUNDERBARER</span>
      <span class="title-line title-large title-season">SOMMER</span>
      <span class="title-line title-small title-in">IN</span>
      <span class="title-line title-large title-place">WEILERTAL</span>
    </h1>
    <div class="cover-illustration" role="img" aria-label="Illustration eines roten Motorrollers mit cremefarbenem Sitz, der lange Schatten auf den blauen Grund wirft"></div>
    <p class="author-name">BERNHARD KOLWITZ</p>
  </main>
</body>
</html>
```